Inspirational quotes poster shop seeks poster designs

Hi! We are launching an eshop with design posterss featuring inspirational quotes. We need a first poster design while looking for further cooperation on around 20 poster designs. We need outputs in the format that can go to high quality print (size at least 100x70cm).

For the first design feel free to choose any of the following quotes to depict:

1. "Stop starting. Start finishing." Author: Torvald Essunger, Klangora
2. "A problem well stated is a problem half solved." Author: Walter P. Brimsley, American inventor
3. "The best way to predict the future is to invent it." Author: Dale Hubbs, Quince

Designs should be rarther simple, think please of your whole concept and how various posters would go together. Every poster can be quite different though, in terms of fonts, colours and overall design, together they should however form and interesting collage.

Designs must contain the quote, author & company. it can be pure text or some indication of the sense of the quote.

Design must also feature company name/logo (not available yet, for now please use "thoughtvolta" as a working name), QR code with a title "Read the story"

See these posters for design we like (for inspiration ONLY!):
http://www.launchtonics.example/products/launch-print-its-simple-until-you-make-it-complicated
http://www.launchtonics.example/products/launch-print-marcus-feldane-less-meetings-more-doing
http://www.launchtonics.example/products/launch-print-gordon-ashfeld-stop-sketching-start-building

Hi to everybody! Sorry for the spam, some of you have been struggling with finding the crux in the quote, so here I offer some ideas what to look for in them. It's up to you to take it, leave it or change it:)

Stop starting, start finishing -
1 - stop starting with many times repeated small word starting, perhaps large word starting made of small words starting, with it contrasting start finishing in normal bold font.
2 - STARTING could look quite unfinished, sketchy, especially -ING could look more unfinished then the rest , e.g. just rough indication of outline of the letters, again contrasting with start finishing will clean & neat writting.

Problem well stated is a problem half solved - look for something that is clearer by defining the problem. Perhaps in a simple sketch like here http://www.launchtonics.example/products/launch-print-its-simple-until-you-make-it-complicated  point out a route from a problem (light = flame), to a solution (lightbulb, lightbulb design drawing or something like that).

Anyway, despite preference for simple design, I am still looking for some smart, creative, catchy idea in the design. Check with yourself if it's something you can would want to buy and hang up on your wall.

Good luck to all of you and again, thank you all very much for participation!
Radim

Target Market(s)

businesses of every size, from startups to large corporates seeking culture change or motivation kick up

Industry/Entity Type

Shop

Requirements
Must have
• I strongly prefer portrait orientation of the poster!

Nice to have
• Quotes themselves are often on the edge, teasing, so the design can be.
Should not have
• Try to avoid traditional dialoge bubble for the quote itself as the first obvious idea for depicting a quote.

Avoid using photos (not simple then) or too many colours.

Of course, by no means use a COPY of existing designs I linked to for inspiration. It just shows what we like.

```html
<!DOCTYPE html>
<html lang="en">
<head>
<meta charset="utf-8">
<title>Stop Starting, Start Finishing — Poster</title>
<link href="https://fonts.googleapis.com/css2?family=Montserrat:ital,wght@0,300;0,500;0,700;1,700&display=swap" rel="stylesheet">
<style>
  :root {
    --backdrop: #e4e4e6;
    --paper: #f4f4f4;
    --ink: #111111;
    --ink-soft: #555555;
    --skin-light: #e0a06f;
    --skin-deep: #d4895a;
  }
  * { margin: 0; padding: 0; box-sizing: border-box; }
  html, body {
    width: 1200px;
    height: 1000px;
    overflow: hidden;
    background: var(--backdrop);
  }
  .canvas {
    position: relative;
    width: 1200px;
    height: 1000px;
  }
  .poster {
    position: absolute;
    left: 271px;
    top: 40px;
    width: 548px;
    height: 767px;
    transform: scale(1.2);
    transform-origin: top left;
    background: var(--paper);
    overflow: hidden;
    font-family: "Montserrat", "Helvetica Neue", Arial, sans-serif;
    color: var(--ink);
  }
  .raised-arm {
    position: absolute;
    left: 30px;
    top: 193px;
    width: 125px;
    height: 574px;
    border-radius: 50px 50px 0 0;
    background: linear-gradient(180deg, var(--skin-light), var(--skin-deep));
  }
  .thumbs-up {
    position: absolute;
    left: 410px;
    top: 383px;
    width: 138px;
    height: 127px;
    border-radius: 30px 0 0 30px;
    background: linear-gradient(180deg, var(--skin-light), var(--skin-deep));
  }
  .quote { font-weight: inherit; }
  .line {
    position: absolute;
    left: 165px;
    line-height: 1;
    white-space: nowrap;
    text-transform: uppercase;
  }
  .line--stop {
    top: 211px;
    font-size: 84px;
    font-weight: 300;
  }
  .line--starting {
    top: 293px;
    font-size: 46px;
    font-weight: 300;
  }
  .line--start {
    top: 403px;
    font-size: 62px;
    font-weight: 700;
    letter-spacing: 2px;
  }
  .line--finishing {
    top: 461px;
    font-size: 56px;
    font-weight: 700;
    letter-spacing: -2.5px;
    transform: scaleX(0.8);
    transform-origin: left center;
  }
  .author {
    position: absolute;
    right: 155px;
    top: 523px;
    text-align: right;
    font-size: 12px;
    font-style: italic;
    font-weight: 700;
    line-height: 1.3;
    white-space: nowrap;
  }
  .author__company {
    display: block;
    font-weight: 500;
    font-style: normal;
    font-size: 10px;
    color: var(--ink-soft);
  }
  .story {
    position: absolute;
    right: 36px;
    top: 612px;
    display: flex;
    flex-direction: column;
    align-items: center;
    gap: 5px;
  }
  .story__title {
    font-size: 9px;
    font-weight: 500;
    letter-spacing: 0.5px;
    text-transform: uppercase;
    white-space: nowrap;
  }
  .story__code {
    width: 62px;
    height: 62px;
    border: 3px solid var(--ink);
    background: var(--paper);
  }
  .brand {
    position: absolute;
    right: 36px;
    bottom: 22px;
    display: flex;
    align-items: center;
    gap: 6px;
    font-size: 13px;
    font-weight: 700;
    line-height: 1;
    white-space: nowrap;
  }
  .brand__mark {
    width: 9px;
    height: 9px;
    background: var(--ink);
  }
</style>
</head>
<body>
  <main class="canvas">
    <article class="poster">
      <div class="raised-arm" role="img" aria-label="Illustration of a raised open hand and arm signalling stop"></div>
      <h1 class="quote">
        <span class="line line--stop">Stop</span>
        <span class="line line--starting">Starting</span>
        <span class="line line--start">Start</span>
        <span class="line line--finishing">Finishing</span>
      </h1>
      <p class="author">Torvald Essunger<span class="author__company">Klangora</span></p>
      <div class="thumbs-up" role="img" aria-label="Illustration of a hand giving a thumbs up"></div>
      <aside class="story">
        <p class="story__title">Read the story</p>
        <div class="story__code" role="img" aria-label="QR code linking to the story behind the quote"></div>
      </aside>
      <footer class="brand"><span class="brand__mark"></span>thoughtvolta</footer>
    </article>
  </main>
</body>
</html>
```